Business Card Design

We need a business card design for a consulting firm which provides safety and risk management consulting services for public venues, hotels and tourist attractions. The business card design should include the attached logo unedited with a design based on incorporating the existing logo with a design of geometric patterns or lines on a predominantly white background.

Industry/Entity Type

Business

Contact Information for Business Card

Dane Morravik
Director & Principal Consultant

Ph: +61 (0) 478506 214
PO Box 456 Brenmoor Vale, NSW Australia 2611
info@corvalrisksafety.example

(back of card to include website www.corvalrisksafety.example

```html
<!DOCTYPE html>
<html lang="en">
<head>
<meta charset="utf-8">
<title>Corval Risk &amp; Safety — Business Card</title>
<link href="https://fonts.googleapis.com/css2?family=Open+Sans:wght@300;400;600;700&display=swap" rel="stylesheet">
<style>
  :root {
    --page: #e9eaec;
    --card: #ffffff;
    --brand-blue: #1c9ed8;
    --brand-green: #7cc143;
    --ink: #3a3d42;
    --ink-soft: #6b6f75;
    --white: #ffffff;
  }
  * { box-sizing: border-box; margin: 0; padding: 0; }
  html, body {
    width: 1200px; height: 948px; overflow: hidden;
    background: var(--page);
    font-family: "Open Sans", Arial, sans-serif;
  }
  .sheet {
    width: 1200px; height: 948px;
    display: flex; flex-direction: column; align-items: center;
    justify-content: center; gap: 48px;
  }
  .card {
    position: relative;
    width: 700px; height: 400px;
    background: var(--card);
    overflow: hidden;
    box-shadow: 0 6px 18px rgba(0,0,0,0.12);
  }

  /* Brand name lockup */
  .brand {
    display: flex; align-items: center; gap: 12px;
  }
  .brand-dot {
    width: 34px; height: 34px; border-radius: 50%;
    background: var(--brand-green); flex: none;
  }
  .brand-name {
    color: var(--brand-blue); font-weight: 700;
    font-size: 30px; letter-spacing: 1px; line-height: 1;
  }

  /* Front */
  .front .brand { position: absolute; left: 44px; top: 52px; }
  .front-band {
    position: absolute; left: 0; right: 0; top: 178px; bottom: 0;
    background: var(--brand-blue);
  }
  .name-tag {
    position: absolute; left: 300px; right: 0; top: 158px; height: 66px;
    background: var(--brand-green);
    padding: 10px 22px;
    color: var(--white);
  }
  .name-tag .person { font-weight: 700; font-size: 20px; line-height: 1.2; }
  .name-tag .role { font-weight: 400; font-size: 14px; line-height: 1.4; }
  .contact {
    position: absolute; left: 300px; top: 244px;
    list-style: none; color: var(--white);
    font-size: 14px; font-weight: 400; line-height: 1.55;
  }
  .contact li { display: flex; align-items: center; gap: 10px; }
  .contact li.plain { padding-left: 24px; }
  .contact svg { width: 14px; height: 14px; flex: none; }

  /* Back */
  .back {
    display: flex; flex-direction: column; align-items: center; justify-content: center;
    gap: 30px;
  }
  .back .brand-name { font-size: 40px; }
  .back .brand-dot { width: 44px; height: 44px; }
  .website {
    color: var(--ink); font-size: 17px; font-weight: 400; letter-spacing: 4px;
  }
</style>
</head>
<body>
<main class="sheet">

  <section class="card front" aria-label="Business card front">
    <div class="brand">
      <span class="brand-dot"></span>
      <span class="brand-name">CORVAL RISK &amp; SAFETY</span>
    </div>
    <div class="front-band"></div>
    <div class="name-tag">
      <div class="person">Dane Morravik</div>
      <div class="role">Director &amp; Principal Consultant</div>
    </div>
    <ul class="contact">
      <li>
        <svg viewBox="0 0 16 16" aria-hidden="true"><circle cx="8" cy="8" r="8" fill="#ffffff"/><path d="M5.2 4.2l1.4-.4.9 2-1 .7c.5 1.1 1.3 1.9 2.4 2.4l.7-1 2 .9-.4 1.4c-3.3.1-6.1-2.7-6-6z" fill="#1c9ed8"/></svg>
        +61 (0) 478506 214
      </li>
      <li>
        <svg viewBox="0 0 16 16" aria-hidden="true"><circle cx="8" cy="8" r="8" fill="#ffffff"/><rect x="4" y="5.2" width="8" height="5.6" fill="none" stroke="#1c9ed8" stroke-width="1.2"/><path d="M4 5.4l4 3 4-3" fill="none" stroke="#1c9ed8" stroke-width="1.2"/></svg>
        info@corvalrisksafety.example
      </li>
      <li class="plain">PO Box 456 Brenmoor Vale</li>
      <li class="plain">NSW Australia 2611</li>
    </ul>
  </section>

  <section class="card back" aria-label="Business card back">
    <div class="brand">
      <span class="brand-dot"></span>
      <span class="brand-name">CORVAL RISK &amp; SAFETY</span>
    </div>
    <div class="website">www.corvalrisksafety.example</div>
  </section>

</main>
</body>
</html>
```